House-share and Room Rental Website (With Focus on the Bedroom Landing Page)

Looking for website design for our House-share (executive accommodation) and room rental business.

Our company name is: Lodvenra could also be written as LodVenra or lodvenra. Either is fine .. just looking for a nice clean catchy logo to go with the design.

EXAMPLES
These are examples of other websites in this field that are doing well. this is a kind of baseline.
https://kelbrin.com.au/
https://www.tuvaplex.com/
https://www.nestorvi.com/
https://www.quillsa.net/
https://www.pendlebarrow.com.au/

Our business model is to rent rooms to people looking for high-quality accommodation. We fill the gap between those looking to rent rooms and those with rooms to rent. However, our model is slightly different from those already on the market as we looking to fill a massive gap in the market delivering upmarket rooms for rent.(Executive Accommodation) also in the back end will be coupled with a self management process in the back end.

We offer executive style accommodation that stands out above the rest. With special extras like fire safety.. and management processes that create happier homes. We are looking for a web design package that can help us grow and scale our business. We need a design that is captivating

Our MAIN focus is having a room landing page that stands out from the rest... The core of our business will rely on the promotion of the rooms in a share house... so the whole design relies on the BEDROOM landing page to drive results.

Target Market(s)

We have 2 markets we are aiming at ... the first market is people offering rooms to rent who want the highest rental return. The second market is people looking to rent safe, high-quality rooms, in houses that are well managed and looked after.

Industry/Entity Type

Share Economy

Logo Text

LodVenra

Number of Pages Required

5+ page

Font styles to use
Sans Serif

Colors
3276b5

Requirements
Must have
• A messaging system whereby we can create direct communication between those offering rooms and those looking for rooms.
• A call to action that says " Schedule an Inspection"
• Landing page for promoting rooms
• A home page for showing stock.
• Profile page for those selling rooms
• Profile page for those looking for rooms.
• A scheduling calendar for booking inspections
Nice to have
• Pages where new residents can lock in a room.. pay bond and rents.. and sign contracts
• Notifications
• SMS capabilities in the backend.
Should not have
• No script or handwriting fonts.

```html
<!DOCTYPE html>
<html lang="en">
<head>
<meta charset="utf-8">
<title>LodVenra – Public amenities</title>
<link href="https://fonts.googleapis.com/css2?family=Dosis:wght@300;400;500;600&display=swap" rel="stylesheet">
<style>
  :root {
    --brand: #3276b5;
    --brand-soft: rgba(50, 118, 181, 0.55);
    --ink: #2b2b2b;
    --ink-muted: #9b9b9b;
    --page: #ffffff;
    --footer-bg: #333333;
    --footer-text: #9d9d9d;
    --footer-heading: #ffffff;
    --map-tone: #ececec;
    --payment-tone: #777777;
  }
  * { box-sizing: border-box; margin: 0; padding: 0; }
  html, body {
    width: 1200px; height: 1000px; overflow: hidden;
    background: var(--page);
    font-family: "Dosis", "Trebuchet MS", sans-serif;
  }
  .amenities {
    position: relative; height: 554px;
  }
  .amenities__content {
    position: absolute; left: 109px; top: 48px; width: 430px;
  }
  .amenities__title {
    font-weight: 300; font-size: 47px; line-height: 54px;
    color: var(--ink); letter-spacing: -0.3px;
  }
  .amenities__lead {
    margin-top: 22px; font-size: 14px; line-height: 22.6px;
    font-weight: 500; color: var(--ink);
  }
  .amenities__note {
    margin-top: 23px; font-size: 14px; line-height: 22.6px;
    color: var(--ink-muted);
  }
  .amenities__list {
    list-style: none; margin-top: 26px;
  }
  .amenities__list li {
    position: relative; padding-left: 24px;
    font-size: 16px; line-height: 33px; font-weight: 400; color: var(--ink);
  }
  .amenities__list li::before {
    content: ""; position: absolute; left: 1px; top: 14px;
    width: 6px; height: 6px; border-radius: 50%;
    border: 1.3px solid var(--brand);
  }
  .location-map {
    position: absolute; left: 602px; top: 58px; width: 488px; height: 374px;
    background: linear-gradient(135deg, #f1f1f1, #e4e4e4 55%, #ededed);
    border: 1px solid #dcdcdc;
    box-shadow: 0 14px 30px rgba(0,0,0,0.12);
    overflow: hidden;
  }
  .location-map__marker {
    position: absolute; left: 174px; top: 118px; width: 141px; height: 141px;
    border-radius: 50%; background: var(--brand-soft);
    display: flex; align-items: center; justify-content: center;
    color: #fff; font-size: 23px; font-weight: 400; letter-spacing: 0.2px;
  }
  .location-map__zoom {
    position: absolute; left: 5px; top: 284px; width: 30px; height: 60px;
    background: #fff; box-shadow: 0 1px 4px rgba(0,0,0,0.25);
  }
  .location-map__zoom span {
    display: block; height: 30px; text-align: center;
    font: 600 22px/30px "Dosis", sans-serif; color: #555;
  }
  .location-map__zoom span + span { border-top: 1px solid #e6e6e6; }

  .site-footer {
    position: absolute; left: 0; top: 554px; width: 1200px; height: 446px;
    background: var(--footer-bg);
  }
  .about {
    position: absolute; left: 109px; top: 96px; width: 420px;
  }
  .about__title {
    font-size: 33px; font-weight: 600; line-height: 40px;
    color: var(--footer-heading);
  }
  .about__text {
    margin-top: 23px; font-size: 14.3px; line-height: 22.6px;
    color: var(--footer-text);
  }
  .copyright {
    position: absolute; left: 109px; top: 317px;
    font-size: 14px; color: var(--brand);
  }
  .social {
    position: absolute; right: 110px; top: 110px; text-align: right;
  }
  .social__title {
    font-size: 19px; font-weight: 600; color: var(--footer-heading);
  }
  .social__links {
    display: flex; gap: 11px; margin-top: 31px; justify-content: flex-end;
  }
  .social__link {
    width: 38px; height: 38px; border-radius: 50%;
    background: var(--brand);
    box-shadow: 0 3px 6px rgba(0,0,0,0.35);
    display: flex; align-items: center; justify-content: center;
    color: #fff; font-size: 16px; font-weight: 600; text-decoration: none;
  }
  .payments {
    position: absolute; right: 110px; top: 317px;
    display: flex; gap: 16px;
    font-size: 13px; font-weight: 600; color: var(--payment-tone);
  }
</style>
</head>
<body>
  <section class="amenities">
    <div class="amenities__content">
      <h1 class="amenities__title">Public amenities</h1>
      <p class="amenities__lead">Transport options available lorem ipsum, lobortis quis mauris et, dignissim ullamcorper nisl. Nunc nec felis a turpis congue molestie ac id orci. Donec venenatis est eget ultrices gravida. Praesent porttitor commodo hendrerit. Mauris laoreet urna in quam lacinia tincidunt.</p>
      <p class="amenities__note">Pellentesque habitant morbi tristique senectus et netus et malesuada fames ac turpis egestas. Duis ultrices egestas erat eget rhoncus.</p>
      <ul class="amenities__list">
        <li>Trains</li>
        <li>Busses</li>
        <li>1 Km to the Sydney harbour bridge</li>
        <li>Shortest route to the city.</li>
      </ul>
    </div>
    <div class="location-map" role="img" aria-label="Street map of the surrounding suburbs with the property location marked">
      <div class="location-map__marker">WE ARE HERE</div>
      <div class="location-map__zoom" aria-hidden="true"><span>+</span><span>−</span></div>
    </div>
  </section>

  <footer class="site-footer">
    <div class="about">
      <h2 class="about__title">About the LodVenra</h2>
      <p class="about__text">Lorem ipsum dolor sit amet, consectetur adipiscing elit. Duis sit amet metus laoreet, sollicitudin quam vitae, varius nisl. Etiam laoreet at quam vel vestibulum. Suspendisse efficitur eros id pharetra malesuada. Morbi nec ipsum nec lectus pretium viverra ut eget diam. Integer id nisi purus. Fusce nisl ipsum, pellentesque eget pharetra vitae, tincidunt id neque. Aliquam nisl metus, consequat in malesuada nec, ullamcorper a eros.</p>
    </div>
    <p class="copyright">© 2019 lodvenra.com.au</p>
    <div class="social">
      <h3 class="social__title">Connect with us</h3>
      <div class="social__links">
        <a class="social__link" href="#" aria-label="Quorvo">Q</a>
        <a class="social__link" href="#" aria-label="Tallyn">T</a>
        <a class="social__link" href="#" aria-label="Framix">F</a>
        <a class="social__link" href="#" aria-label="Boardel">B</a>
      </div>
    </div>
    <div class="payments" aria-label="Accepted payments">
      <span>Velta</span><span>Orbix</span><span>Amvale</span><span>Paydra</span>
    </div>
  </footer>
</body>
</html>
```